Forex Trading Software Sales Page

We need header, footer, mid section and background design for our new website for a forex software that helps people make better decision in forex trading. Simple Sales Page. You can use test name "Meridel Sample Layout" on the design itself.

The new design must be blue tone, corporate, look expensive, show confidence and wealth. Please show us how you can improve our current design style by making something similar to the designed attached or making something entirely different that will better deliver the message to the visitors.

3 Examples of our previous designs are attached.

Target Market(s)

Forex Beginners, People who want to make money at home.

Industry/Entity Type

Business

Number of Pages Required

1 page

Font styles to use
Sans Serif

Colors
0255a3
eaf1f7
ffffff

Requirements
Must have
• The design must be 90% similar to this:
• https://www.quarnelbay7.com/
• 1) Name "Meridel Sample Layout" on header and footer.
• 2) PSDs of header, footer, mid section and background design.
• 3) Images of money bags, stacks etc
• 4) Show wealth, confidence and look expensive
• 5) Blueish tone of website mainly
• 6) Sample of headline and content colors and fonts.
Nice to have
• People will be buying products from this website, so it must not look too cheesy or over promising. Must give confidence and look expensive and clean.
Should not have
• Images of cars, yachts, villas or anything else that is associated with being rich.

```html
<!DOCTYPE html>
<html lang="en">
<head>
<meta charset="utf-8">
<title>Meridel Sample Layout – Sales Page</title>
<link rel="stylesheet" href="https://fonts.googleapis.com/css2?family=Oswald:wght@400;500;600;700&family=Open+Sans:wght@400;600;700&display=swap">
<style>
:root{
  --navy-deep:#0e2647;
  --navy-band:#0b2a55;
  --page-bg:#eaf1f7;
  --brand-blue:#0255a3;
  --title-blue:#2f6aa6;
  --accent-yellow:#f2ef12;
  --button-yellow:#f5f000;
  --headline-red:#7a0b0b;
  --ink:#1a1a1a;
  --white:#ffffff;
  --sell-orange:#f08a12;
}
*{box-sizing:border-box;margin:0;padding:0}
html,body{width:678px;height:1200px;overflow:hidden;background:var(--page-bg)}
.page{position:relative;width:678px;height:1200px;overflow:hidden;background:var(--page-bg);font-family:"Open Sans",Arial,sans-serif;color:var(--ink)}
.abs{position:absolute}

/* Header */
.header-art{left:0;top:0;width:678px;height:300px}
.site-title{left:0;width:678px;top:20px;padding-left:26px;text-align:center;color:var(--white);font-family:"Oswald",sans-serif;font-weight:600;font-size:46px;line-height:48px;text-transform:uppercase;letter-spacing:.5px}

/* Hero */
.hero-headline{left:86px;top:292px;width:236px;text-align:center;font-family:"Oswald",sans-serif;font-weight:500;text-transform:uppercase;line-height:1.14;color:var(--ink)}
.hero-headline .l1,.hero-headline .l2,.hero-headline .l5,.hero-headline .l6{font-size:19px}
.hero-headline .l3,.hero-headline .l4{font-size:23px}
.hero-headline .red{color:var(--headline-red)}
.hero-headline .l6{text-align:left}
.video-caption{left:346px;top:260px;width:243px;text-align:center;font-family:"Oswald",sans-serif;font-weight:500;font-size:13px;color:var(--headline-red)}
.video-chart{left:346px;top:282px;width:243px;height:164px;border:1px solid #444}

/* Order row */
.pay-badge{width:37px;height:37px;border-radius:50%;background:var(--white);box-shadow:0 1px 3px rgba(0,0,0,.25);display:flex;align-items:center;justify-content:center;font-family:"Open Sans",sans-serif;font-weight:700;font-size:7.5px;color:var(--brand-blue);top:487px}
.order-button{left:246px;top:472px;width:239px;height:62px;border:4px solid var(--button-yellow);background:var(--white);display:flex;align-items:center;justify-content:center;font-family:"Oswald",sans-serif;font-weight:500;font-size:33px;color:var(--brand-blue);text-decoration:none}
.download-link{left:0;width:678px;top:543px;text-align:center;font-size:12px;font-weight:600;color:var(--ink);text-decoration:underline}

/* Mid section */
.section-title{left:0;width:678px;top:584px;text-align:center;font-family:"Oswald",sans-serif;font-weight:600;font-size:22px;line-height:25px;color:var(--title-blue);text-transform:uppercase}
.section-rule{top:623px;height:1px;background:#333;width:87px}
.product-box{left:92px;top:690px;width:184px;height:234px;background:linear-gradient(160deg,#1b3f7a 0%,#2a6a8a 35%,#c9b88a 70%,#6f7d5a 100%)}
.product-copy{left:296px;top:684px;width:296px;font-size:12.4px;line-height:14.6px;color:#222}
.product-copy p{margin-bottom:14.6px}
.product-copy .blue{color:var(--brand-blue)}
.product-copy .orange{color:var(--sell-orange)}
.product-copy strong{font-weight:700}

/* Footer */
.footer-band{left:0;top:939px;width:678px;height:23px;background:var(--navy-band);text-align:center;font-family:"Oswald",sans-serif;font-weight:500;font-size:13.5px;line-height:23px;text-transform:uppercase;color:var(--white)}
.footer-band .yellow{color:var(--accent-yellow)}
.footer-bg{left:0;top:962px;width:678px;height:238px;background:linear-gradient(135deg,#223e62 0%,#1a3354 50%,#243f63 100%)}
.footer-title{left:60px;width:196px;top:988px;text-align:center;color:var(--white);font-family:"Oswald",sans-serif;font-weight:600;font-size:40px;line-height:46px;text-transform:uppercase}
.promise{left:296px;height:36px;display:flex;align-items:center;gap:14px;font-family:"Oswald",sans-serif;font-weight:500;font-size:11.5px;color:var(--accent-yellow);text-transform:uppercase}
.promise svg{width:36px;height:36px}
.footer-links{left:552px;top:1026px;list-style:none;font-size:7.5px;line-height:18px;color:var(--white)}
.retailer-mark{left:90px;top:1148px;width:36px;height:36px;border-radius:50%;background:var(--white);display:flex;align-items:center;justify-content:center;font-size:6px;font-weight:700;color:var(--brand-blue)}
.retailer-note{left:142px;top:1150px;width:348px;font-size:5.6px;line-height:6.2px;color:#e6ecf3}
.social-row{left:505px;top:1156px;display:flex;gap:12px;list-style:none}
.social{display:flex;align-items:center;gap:4px;font-size:7.5px;font-weight:600;color:var(--white)}
.social i{display:block;width:8px;height:8px;border-radius:50%;background:var(--white)}
</style>
</head>
<body>
<div class="page">

  <!-- Header -->
  <svg class="abs header-art" viewBox="0 0 678 300">
    <defs>
      <linearGradient id="moneyTone" x1="0" y1="0" x2="1" y2="1">
        <stop offset="0" stop-color="#2a4669"/>
        <stop offset=".5" stop-color="#1c3658"/>
        <stop offset="1" stop-color="#29466b"/>
      </linearGradient>
    </defs>
    <g role="img" aria-label="Scattered banknotes in deep blue tone">
      <polygon points="0,0 678,0 678,140 0,264" fill="url(#moneyTone)"/>
    </g>
    <polygon points="0,264 678,140 678,161 0,292" fill="var(--navy-deep)"/>
    <text transform="translate(364 214) rotate(-10.4)" text-anchor="middle" font-family="Oswald, sans-serif" font-weight="500" font-size="14.5" fill="#f2ef12">HIGHLY PROFITABLE INDICATOR WITH <tspan fill="#ffffff">EASY-TO-FOLLOW SIGNALS</tspan></text>
  </svg>
  <h1 class="abs site-title">Meridel<br>Sample<br>Layout</h1>

  <!-- Hero -->
  <div class="abs hero-headline">
    <div class="l1"><span class="red">New trading secret</span> that is</div>
    <div class="l2">able to accurately predict</div>
    <div class="l3 red">a new trend before it</div>
    <div class="l4 red">even starts!</div>
    <div class="l5">and generate a fast <span class="red">buy or</span></div>
    <div class="l6"><span class="red">sell</span> signal!</div>
  </div>

  <div class="abs video-caption">+786 Pips Live Action Video</div>
  <svg class="abs video-chart" viewBox="0 0 243 164">
    <rect width="243" height="164" fill="#050505"/>
    <g stroke="#2a2a2a" stroke-width="1">
      <line x1="0" y1="20" x2="243" y2="20"/><line x1="0" y1="45" x2="243" y2="45"/>
      <line x1="0" y1="70" x2="243" y2="70"/><line x1="0" y1="95" x2="243" y2="95"/>
      <line x1="0" y1="120" x2="243" y2="120"/><line x1="0" y1="145" x2="243" y2="145"/>
      <line x1="30" y1="0" x2="30" y2="164"/><line x1="60" y1="0" x2="60" y2="164"/>
      <line x1="90" y1="0" x2="90" y2="164"/><line x1="120" y1="0" x2="120" y2="164"/>
      <line x1="150" y1="0" x2="150" y2="164"/><line x1="180" y1="0" x2="180" y2="164"/>
      <line x1="210" y1="0" x2="210" y2="164"/>
    </g>
    <text x="4" y="7" font-size="4" fill="#bbb" font-family="Open Sans, sans-serif">EURUSD,H4 1.0578 1.0712 1.0560 1.0698</text>
    <g stroke="#34c234" stroke-width="1">
      <line x1="26" y1="90" x2="26" y2="130"/><line x1="34" y1="95" x2="34" y2="125"/>
      <line x1="48" y1="80" x2="48" y2="118"/><line x1="58" y1="70" x2="58" y2="110"/>
      <line x1="72" y1="55" x2="72" y2="100"/><line x1="84" y1="45" x2="84" y2="92"/>
      <line x1="96" y1="40" x2="96" y2="80"/><line x1="108" y1="18" x2="108" y2="70"/>
      <line x1="116" y1="15" x2="116" y2="50"/><line x1="124" y1="20" x2="124" y2="45"/>
    </g>
    <g fill="#34c234">
      <rect x="24" y="100" width="4" height="22"/><rect x="46" y="88" width="4" height="20"/>
      <rect x="70" y="62" width="4" height="28"/><rect x="94" y="48" width="4" height="22"/>
      <rect x="106" y="26" width="4" height="34"/><rect x="122" y="26" width="4" height="12"/>
    </g>
    <g fill="#ffffff">
      <rect x="32" y="104" width="4" height="14"/><rect x="56" y="78" width="4" height="22"/>
      <rect x="82" y="55" width="4" height="26"/><rect x="114" y="22" width="4" height="18"/>
    </g>
    <path d="M19 152 C40 125 60 115 80 100 S105 80 112 62 S118 45 124 38" fill="none" stroke="#2fa3e6" stroke-width="1.6"/>
    <circle cx="19" cy="152" r="2.5" fill="#2fa3e6"/>
    <line x1="0" y1="113" x2="12" y2="113" stroke="#f08a12" stroke-width="1.5"/>
    <rect x="65" y="89" width="85" height="25" rx="5" fill="#1f7ae0" stroke="#9cc8f5" stroke-width="1"/>
    <text x="107.5" y="106" text-anchor="middle" font-family="Open Sans, sans-serif" font-weight="700" font-size="12.5" fill="#fff">+152 Pips!</text>
    <polygon points="145,80 152,84 145,88" fill="#fff"/>
  </svg>

  <!-- Order row -->
  <div class="abs pay-badge" style="left:90px">Halden</div>
  <div class="abs pay-badge" style="left:141px">Corvin</div>
  <div class="abs pay-badge" style="left:192px">Ostrel</div>
  <a class="abs order-button" href="https://www.quarnelbay7.com/">Order Now</a>
  <div class="abs pay-badge" style="left:500px">Brask</div>
  <div class="abs pay-badge" style="left:552px">Quillon</div>
  <a class="abs download-link" href="https://www.quarnelbay7.com/">Click Here to download “Trendline Scout Pro” right now!</a>

  <!-- Mid section -->
  <h2 class="abs section-title">Meridel<br>Sample<br>Layout</h2>
  <div class="abs section-rule" style="left:194px"></div>
  <div class="abs section-rule" style="left:398px"></div>

  <div class="abs product-box" role="img" aria-label="Software product box with money bags and banknotes"></div>
  <div class="abs product-copy">
    <p>Trendline Scout Pro is a brand new indicator designed for making maximum profit from big price movements.</p>
    <p>It shows two different lines: <span class="blue">blue line</span> indicates a <span class="blue">buy signal</span> and <span class="orange">orange line</span> - <span class="orange">sell signal</span>. On top of that, whenever a new signal is generated, Trendline Scout Pro can alert you via email, pop up (with sound) or push notification sent to your mobile.</p>
    <p><strong>Absolutely No repaint!</strong> If you get a signal - you can be 100% confident that the indicator will not change it. Trendline Scout Pro is designed to help you make stable profit with big confidence and no stress.</p>
  </div>

  <!-- Footer -->
  <div class="abs footer-band"><span class="yellow">Highly profitable indicator with</span> easy-to-follow signals</div>
  <div class="abs footer-bg" role="img" aria-label="Banknotes background in deep blue tone"></div>
  <div class="abs footer-title">Meridel<br>Sample<br>Layout</div>

  <div class="abs promise" style="top:1016px">
    <svg viewBox="0 0 36 36"><circle cx="18" cy="18" r="16" fill="none" stroke="#f2ef12" stroke-width="3"/><text x="18" y="25" text-anchor="middle" font-family="Oswald, sans-serif" font-weight="700" font-size="20" fill="#f2ef12">$</text></svg>
    <span>60 days money back guarantee</span>
  </div>
  <div class="abs promise" style="top:1068px">
    <svg viewBox="0 0 36 36"><circle cx="18" cy="18" r="16" fill="none" stroke="#f2ef12" stroke-width="3"/><path d="M12 10 l4 -1 l2 5 l-2.5 2 c1 2.5 3 4.5 5.5 5.5 l2 -2.5 l5 2 l-1 4 c-8 1 -16 -7 -15 -15z" fill="none" stroke="#f2ef12" stroke-width="1.8" stroke-linejoin="round"/></svg>
    <span>24/7 online customer support</span>
  </div>

  <ul class="abs footer-links">
    <li>About Us</li><li>FAQ</li><li>Disclaimer</li><li>Affiliates</li><li>Contact Us</li>
  </ul>

  <div class="abs retailer-mark">Vantorel</div>
  <p class="abs retailer-note">Vantorel is the retailer of products on this site. VANTOREL is a registered trademark of Harlow Sales, Inc., a Delaware corporation located at 42 Ormond Lane, Suite 110, Fenwick, 55120, USA and used by permission. Vantorel's role as retailer does not constitute an endorsement, approval or review of these products or any claim, statement or opinion used in promotion of these products. All rights reserved © 2017</p>

  <ul class="abs social-row">
    <li class="social"><i></i>Ebbe</li>
    <li class="social"><i></i>Solna</li>
    <li class="social"><i></i>Ruvo</li>
  </ul>

</div>
</body>
</html>
```